Belzo business card

I'm a hack at Illustrator, but have put together a set of business cards as attached. If someone could please improve these including good font selection, standard font sizes and spacing, nice layout and symmetry. Rear side the same on all cards. Basically make these cards into something impressive and professional.
Updates

Official logo just uploaded, please use these colours

Target Market(s)

50+ year old married couples

Industry/Entity Type

Business

Requirements
Must have
• Professional
Should not have
• Silly, cartoony

```html
<!DOCTYPE html>
<html lang="en">
<head>
<meta charset="utf-8">
<title>Belzo business card</title>
<link href="https://fonts.googleapis.com/css2?family=Arimo:wght@400;700&family=Tinos&display=swap" rel="stylesheet">
<style>
  :root {
    --brand-blue: #2b3990;
    --ink: #1f1f1f;
    --paper: #ffffff;
    --backdrop: #e9ebef;
    --rule: #8a8a8a;
  }
  * { margin: 0; padding: 0; box-sizing: border-box; }
  html, body {
    width: 1200px; height: 900px; overflow: hidden;
    background: var(--backdrop);
  }
  .canvas { position: relative; width: 1200px; height: 900px; }

  .card {
    position: absolute;
    width: 640px; height: 366px;
    background: var(--paper);
    box-shadow: 0 6px 18px rgba(0,0,0,0.12);
    overflow: hidden;
  }

  .company-name {
    font-family: "Arimo", sans-serif;
    font-weight: 700;
    color: var(--brand-blue);
    line-height: 1;
  }

  /* Name side */
  .card-name-side { left: 80px; top: 70px; }
  .card-name-side .company-name {
    position: absolute; left: 0; top: 150px; width: 640px;
    text-align: center; font-size: 60px;
  }

  /* Details side */
  .card-details-side { left: 480px; top: 464px; }
  .details-body { position: absolute; left: 0; top: 0; width: 640px; height: 264px; }
  .person { position: absolute; left: 96px; top: 66px; font-family: "Tinos", serif; color: var(--ink); }
  .person-name { font-size: 28px; font-weight: 400; margin-bottom: 8px; }
  .person-role { font-size: 14px; line-height: 23px; }
  .divider { position: absolute; left: 320px; top: 100px; width: 1px; height: 104px; background: var(--rule); }

  .card-details-side .company-name {
    position: absolute; left: 420px; top: 40px; font-size: 30px;
  }

  .contact {
    position: absolute; left: 368px; top: 172px;
    font-family: "Tinos", serif; font-size: 14px; line-height: 22px; color: var(--ink);
  }

  .address-band {
    position: absolute; left: 0; bottom: 0; width: 640px; height: 102px;
    background: var(--brand-blue); color: var(--paper);
    font-family: "Arimo", sans-serif; font-weight: 700; text-align: center;
    padding-top: 14px;
  }
  .address-band p { font-size: 18px; line-height: 27px; }
  .band-web { font-size: 17px; }
  .band-reg { font-size: 13px; margin-left: 18px; }
</style>
</head>
<body>
<main class="canvas">

  <section class="card card-name-side" aria-label="Card front">
    <p class="company-name">Belzo</p>
  </section>

  <section class="card card-details-side" aria-label="Card details side">
    <div class="details-body">
      <div class="person">
        <h1 class="person-name">Daniel Harper</h1>
        <p class="person-role">General Manager<br>Building &amp; Technology<br>Innovator</p>
      </div>
      <div class="divider"></div>
      <p class="company-name">Belzo</p>
      <div class="contact">
        <p>M: 0412 555 018</p>
        <p>D: 03 9555 0142</p>
        <p>daniel.harper@belzo.com.au</p>
      </div>
    </div>
    <footer class="address-band">
      <p>8 / 40 Elm Street, Brookvale, VIC 3199, Australia.</p>
      <p>Ph : (+61) 03 9555 0100</p>
      <p><span class="band-web">www.belzo.co.au</span><span class="band-reg">REC 40817 ABN XXXXXXXXXXXXXX</span></p>
    </footer>
  </section>

</main>
</body>
</html>
```